Tallyden Web Design

Create Website Design for Tallyden. Tallyden is online application for collaboration team work system (task list management). More concept design for this project please find attach file ("tallyden website concept.pdf") . But my concept is just describe minimal features not bind design

For tallyden logo, i had already attach files. But i had not decided what color i chose, so it's okay if you suggest logo color for your suitable website design.
Updates

Dear All Designer,

I like brisk carousel (http://quillforge-labs.example/brisk-carousel/),
may be your concept design can adjust with this concept.
but don't worry about script for brisk carousel, my team will be handle
You just make website design to suitable with brisk carousel

but if you had own website design concept are welcome

thanks

Target Market(s)

Business Company

Industry/Entity Type

Management

```html
<!DOCTYPE html>
<html lang="en">
<head>
<meta charset="utf-8">
<title>Tallyden</title>
<link rel="stylesheet" href="https://fonts.googleapis.com/css2?family=Open+Sans:wght@400;600;700&family=Signika:wght@300;400;600&family=Lora:wght@400;700&display=swap">
<style>
:root{
  --green:#6a9a2a;
  --teal:#2e8f86;
  --orange:#f07a1f;
  --nav-active:#f06a1a;
  --text:#4a4a4a;
  --dark:#222;
  --beige:#f1ede4;
  --line:#e0ddd5;
  --blue-light:#8cc8e8;
  --blue-band:#5fa7d4;
  --blue-dark:#2f6fa5;
  --login:#1f7f6d;
}
*{margin:0;padding:0;box-sizing:border-box}
html,body{width:1200px;height:2185px;overflow:hidden}
body{position:relative;background:#fff;font-family:"Open Sans",Arial,sans-serif;color:var(--text)}
.abs{position:absolute}
/* header */
.site-header{left:0;top:0;width:1200px;height:118px;background:#fff}
.brand{left:142px;top:28px;display:flex;align-items:center;gap:12px;font-family:"Signika",sans-serif;font-weight:600;font-size:54px;color:var(--green);line-height:1}
.brand-dot{width:22px;height:22px;border-radius:50%;background:var(--teal)}
.login-btn{left:965px;top:15px;width:91px;height:36px;background:var(--login);border:2px solid #bfe0d8;border-radius:4px;color:#fff;font-weight:700;font-size:15px;display:flex;align-items:center;justify-content:center;gap:7px}
.main-nav{left:473px;top:78px;height:40px;display:flex;border-top:1px solid var(--line);border-left:1px solid var(--line)}
.main-nav a{display:block;padding:0 17px;line-height:38px;font-size:15px;color:var(--dark);text-decoration:none;border-right:1px solid var(--line)}
.main-nav a.active{color:var(--nav-active);font-weight:700}
/* hero */
.hero{left:0;top:118px;width:1200px;height:428px;background:linear-gradient(90deg,#8d95a0 0%,#c9c6c2 25%,#e6e3df 50%,#c7c2bb 75%,#8a8f97 100%)}
.hero-title{left:0;top:146px;width:1200px;text-align:center;font-family:"Lora",serif;font-size:34px;color:#111}
.hero-title em{font-style:normal;font-weight:700;color:var(--orange)}
.hero-screen{left:191px;top:218px;width:820px;height:328px;background:linear-gradient(#eef1f5,#d9dde3);border:1px solid #9aa2ac;box-shadow:0 0 12px rgba(0,0,0,.25)}
/* features */
.features{left:0;top:546px;width:1200px;height:1098px;background:var(--beige)}
.feature-ring{width:330px;height:330px}
.feature-h{font-family:"Signika",sans-serif;font-weight:300;font-size:46px;line-height:1}
.feature-p{width:480px;font-size:15.5px;line-height:22px;color:#555}
.h-green{color:var(--green)} .h-teal{color:var(--teal)} .h-orange{color:var(--orange)}
.divider{left:200px;width:800px;height:1px;background:linear-gradient(90deg,transparent,#d6d1c6,transparent)}
/* lower */
.col-h{font-family:"Signika",sans-serif;font-size:25px;line-height:28px;color:var(--dark);font-weight:600}
.col-h span{display:block;font-weight:300;color:#555}
.col-p{font-size:14px;line-height:22px;color:#555}
.learn{font-size:12px;font-weight:700;color:var(--blue-dark);letter-spacing:.5px}
.quote-mark{font-family:"Lora",serif;font-size:80px;line-height:1;color:#ccc}
.contact-box{left:778px;top:1672px;width:278px;height:309px;background:var(--blue-light);border-radius:4px;padding:0 14px}
.contact-box h3{font-family:"Signika",sans-serif;color:#fff;font-size:21px;font-weight:600;line-height:40px;margin:0 -14px 6px;padding:0 10px;background:#a9d6ee;border-radius:4px 4px 0 0}
.field{height:31px;background:#dbe9f2;border:1px solid #c3d6e2;margin-bottom:6px;font-size:13px;color:#444;padding:6px 8px}
.field.msg{height:72px}
.chars{font-size:12px;color:#333;margin-top:6px}
.captcha{display:flex;gap:8px;margin-top:6px}
.captcha-img{width:120px;height:34px;background:linear-gradient(90deg,#ddd,#f4f4f4,#ccc)}
.captcha-in{flex:1;height:30px;margin-top:4px;background:#dbe9f2;border:1px solid #c3d6e2}
.submit{margin-top:10px;width:58px;height:28px;background:linear-gradient(#ffc13a,#f29a0a);border-radius:3px;color:#fff;font-weight:700;font-size:13px;text-align:center;line-height:28px}
/* footer */
.news-band{left:0;top:2036px;width:1200px;height:51px;background:linear-gradient(#7ab8de,var(--blue-band))}
.social{top:2050px;width:26px;height:26px;border-radius:50%;background:#3e88bd;border:2px solid #cfe6f4}
.join{left:612px;top:2040px;text-align:right;color:#fff;font-family:"Signika",sans-serif;line-height:20px}
.join b{display:block;font-size:14px;font-weight:300;letter-spacing:2px}
.join strong{font-size:19px;font-weight:600}
.news-note{left:775px;top:2039px;font-size:11px;color:#fff;font-weight:600}
.news-input{left:775px;top:2060px;width:224px;height:21px;background:#fff;font-size:11px;color:#555;padding:3px 6px}
.news-btn{left:1002px;top:2060px;width:54px;height:21px;background:#1d5f93;color:#fff;font-size:10px;font-weight:700;text-align:center;line-height:21px}
.site-footer{left:0;top:2087px;width:1200px;height:98px;background:var(--blue-dark);color:#fff}
.foot-nav{left:0;top:2114px;width:1200px;display:flex;justify-content:center;align-items:center;gap:30px;font-size:14px;color:#fff}
.foot-nav .sep{width:1px;height:26px;background:#6a9ccb}
.foot-nav .ico{display:flex;align-items:center;gap:8px}
.legal{left:140px;top:2159px;font-size:12px;color:#fff}
.legal span{padding:0 8px;border-left:1px solid #8ab3d8}
.legal span:first-child{padding-left:0;border:0}
.copy{left:956px;top:2159px;font-size:12px;color:#fff}
</style>
</head>
<body>
<header class="abs site-header">
  <div class="abs brand"><span>tallyden</span><span class="brand-dot"></span></div>
  <div class="abs login-btn">
    <svg width="14" height="14" viewBox="0 0 14 14"><circle cx="7" cy="4" r="3.2" fill="#fff"/><path d="M1 14c0-4 3-6 6-6s6 2 6 6z" fill="#fff"/></svg>LOGIN</div>
  <nav class="abs main-nav">
    <a class="active">Home</a><a>About Us</a><a>Services</a><a>Products</a><a>Testimonials</a><a>Contact Us</a>
  </nav>
</header>

<section>
  <div class="abs hero" role="img" aria-label="Softly blurred photo of a business team collaborating in an office"></div>
  <h1 class="abs hero-title">Customize <em>Online Collaboration</em> Team Work</h1>
  <div class="abs hero-screen" role="img" aria-label="Application window screenshot showing a transaction list table"></div>
</section>

<section class="abs features"></section>

<svg class="abs feature-ring" style="left:145px;top:545px" viewBox="0 0 330 330" role="img" aria-label="Photo of a tablet showing a spreadsheet in hand">
  <circle cx="165" cy="165" r="160" fill="none" stroke="#c9d9b0" stroke-width="1"/>
  <circle cx="165" cy="165" r="145" fill="none" stroke="#b6cf90" stroke-width="1.5"/>
  <circle cx="165" cy="165" r="132" fill="none" stroke="#98bd66" stroke-width="1.5"/>
  <circle cx="165" cy="165" r="118" fill="#fff"/>
  <circle cx="165" cy="165" r="104" fill="#d9e2ea"/>
</svg>
<h2 class="abs feature-h h-green" style="left:513px;top:646px">Customize Application</h2>
<p class="abs feature-p" style="left:513px;top:699px">Lorem ipsum dolor sit amet, consectetur adipisicing elit, sed do eiusmod tempor incididunt ut labore et dolore. magna aliqua. Ut enim ad minim veniam, quis nostrud exercitation ullamco laboris nisi ut aliquip ex ea commodo consequat. Duis aute irure dolor in reprehenderit in voluptate velit esse cillum.</p>
<div class="abs divider" style="top:920px"></div>

<svg class="abs feature-ring" style="left:715px;top:928px" viewBox="0 0 330 330" role="img" aria-label="Photo of a laptop, tablet and phone showing the same app">
  <circle cx="165" cy="165" r="160" fill="none" stroke="#a9d3cd" stroke-width="1"/>
  <circle cx="165" cy="165" r="145" fill="none" stroke="#8cc5bd" stroke-width="1.5"/>
  <circle cx="165" cy="165" r="132" fill="none" stroke="#5aaa9f" stroke-width="1.5"/>
  <circle cx="165" cy="165" r="118" fill="#fff"/>
  <circle cx="165" cy="165" r="104" fill="#d3d8de"/>
</svg>
<h2 class="abs feature-h h-teal" style="left:197px;top:1000px">Synchronize All Device</h2>
<p class="abs feature-p" style="left:197px;top:1053px">Lorem ipsum dolor sit amet, consectetur adipisicing elit, sed do eiusmod tempor incididunt ut labore et dolore. magna aliqua. Ut enim ad minim veniam, quis nostrud exercitation ullamco laboris nisi ut aliquip ex ea commodo consequat. Duis aute irure dolor in reprehenderit in voluptate velit esse cillum.</p>
<div class="abs divider" style="top:1275px"></div>

<svg class="abs feature-ring" style="left:145px;top:1252px" viewBox="0 0 330 330" role="img" aria-label="Illustration of a tablet displaying a report chart with a pen">
  <circle cx="165" cy="165" r="160" fill="none" stroke="#f3cda9" stroke-width="1"/>
  <circle cx="165" cy="165" r="145" fill="none" stroke="#f2b783" stroke-width="1.5"/>
  <circle cx="165" cy="165" r="132" fill="none" stroke="#ee9548" stroke-width="1.5"/>
  <circle cx="165" cy="165" r="118" fill="#fff"/>
  <circle cx="165" cy="165" r="104" fill="#e4e6e8"/>
</svg>
<h2 class="abs feature-h h-orange" style="left:513px;top:1355px">Report</h2>
<p class="abs feature-p" style="left:513px;top:1408px">Lorem ipsum dolor sit amet, consectetur adipisicing elit, sed do eiusmod tempor incididunt ut labore et dolore. magna aliqua. Ut enim ad minim veniam, quis nostrud exercitation ullamco laboris nisi ut aliquip ex ea commodo consequat. Duis aute irure dolor in reprehenderit in voluptate velit esse cillum.</p>

<section>
  <h3 class="abs col-h" style="left:142px;top:1690px">Why<span>Tallyden</span></h3>
  <p class="abs col-p" style="left:140px;top:1750px;width:270px">Lorem ipsum dolor sit amet, consectetur adipisicing elit, sed do eiusmod tempor incididunt ut labore et dolore magna aliqua. Ut enim ad minim veniam, quis nostrud exercitation ullamco laboris nisi ut aliquip ex ea commodo consequat. Duis aute irure dolor in reprehenderit in voluptate velit esse cillum.</p>
  <span class="abs learn" style="left:140px;top:1936px">LEARN MORE</span>

  <h3 class="abs col-h" style="left:448px;top:1690px">Customer<span>Say</span></h3>
  <div class="abs quote-mark" style="left:446px;top:1752px">&#8221;</div>
  <p class="abs col-p" style="left:506px;top:1757px;width:250px">Lorem ipsum dolor sit amet, consectetur adipisicing elit, sed do eiusmod tempor incididunt ut labore et dolore magna aliqua. Ut enim ad minim veniam, quis nostrud exercitation ullamco laboris nisi ut aliquip ex ea commodo.</p>
  <p class="abs col-p" style="left:503px;top:1922px;color:#333">John Doe, Some Business</p>

  <form class="abs contact-box">
    <h3>Quick Contact</h3>
    <div class="field">Enter your name</div>
    <div class="field">Enter your email</div>
    <div class="field msg">Enter a message</div>
    <div class="chars"><b>5000</b> characters left</div>
    <div class="captcha"><div class="captcha-img" role="img" aria-label="Captcha image"></div><div class="captcha-in"></div></div>
    <div class="submit">Submit</div>
  </form>
</section>

<footer>
  <div class="abs news-band"></div>
  <div class="abs social" style="left:141px"></div>
  <div class="abs social" style="left:178px"></div>
  <div class="abs join"><b>JOIN US</b><strong>OUR NEWSLETTER</strong></div>
  <div class="abs news-note">Services updates and special offers in your mailbox!</div>
  <div class="abs news-input">Email Address</div>
  <div class="abs news-btn">SIGN UP</div>
  <div class="abs site-footer"></div>
  <nav class="abs foot-nav">
    <span>Home</span><span>About Us</span><span>Products</span><span>Testimonials</span><span>Contact Us</span>
    <span class="sep"></span>
    <span class="ico"><svg width="20" height="20" viewBox="0 0 20 20"><path d="M4 2l4 4-2 3c1 2 3 4 5 5l3-2 4 4-3 3C9 19 1 11 1 5z" fill="#fff"/></svg>(555) 013-2847</span>
    <span class="sep"></span>
    <span class="ico"><svg width="18" height="14" viewBox="0 0 18 14"><rect x="1" y="1" width="16" height="12" fill="none" stroke="#fff" stroke-width="1.6"/><path d="M1 1l8 7 8-7" fill="none" stroke="#fff" stroke-width="1.6"/></svg>info@tallyden.com</span>
  </nav>
  <div class="abs legal"><span>Disclaimer</span><span>Terms &amp; Conditions</span><span>Privacy Policy</span><span>Site Map</span></div>
  <div class="abs copy">© 2013 Tallyden.</div>
</footer>
</body>
</html>
```